Bright Thread Pty Ltd Brochure and New Image Design

Initally we will be needing a A4 Folder design created as well as a Template for a Double Sided Flyer. We need a cutting edge design which we can incorporate into a Brochure, Flyer Handout, Website etc. Basically we are re-branding our company starting with an "About Us" Folder which we will be distributing to potential customers.
We are an Embroidery company that caters for mid-large companies dealing with clothing ranging from Corporate Attire to Workwear. Our current website has more information on what we do and you can use that as a valid reference point (www.brightthreadco.com.au), However the website will be step 2 in freshening up our image.
Our company has been thriving over the 20 years we have been in business by supplying a higher quality product as well as Service that is second to none, unfortunately our branding image has been overlooked while we have spent more time/effort on our customer service.
We have used the colours Maroon (PMS 216C) Silver Grey (PMS Cool Gray 7) White and Black. We would like to maintain these colours but incorporate them together in a way that has a more "modern edgey" look.
Target Market(s)
Purchasing / Marketing Officers of Mid-Large Corporate Companies.
Industry/Entity Type
Clothing
Look and feel

```html
<!DOCTYPE html>
<html lang="en">
<head>
<meta charset="utf-8">
<title>Bright Thread – Folder and Letterhead</title>
<link href="https://fonts.googleapis.com/css2?family=Cabin:wght@500;600&display=swap" rel="stylesheet">
<style>
  :root {
    --maroon: #850a4a;
    --maroon-soft: #e7cfe0;
    --pocket-purple: #93278f;
    --silver: #c6c7c9;
    --paper: #ffffff;
    --stage: #eeeeef;
    --text-font: "Cabin", "Trebuchet MS", sans-serif;
  }
  * { box-sizing: border-box; margin: 0; padding: 0; }
  html, body { width: 1200px; height: 900px; overflow: hidden; }
  body { background: var(--stage); font-family: var(--text-font); position: relative; }

  .brand-mark {
    position: absolute;
    display: flex; align-items: center; justify-content: center;
    border: 2px solid var(--maroon);
    border-radius: 4px;
    color: var(--maroon);
    font-weight: 600;
    background: var(--paper);
    white-space: nowrap;
  }

  /* Letterhead */
  .letterhead {
    position: absolute; left: 50px; top: 215px;
    width: 340px; height: 480px;
    background: var(--paper);
    box-shadow: 0 4px 14px rgba(0,0,0,.25);
  }
  .letterhead .top-rule {
    position: absolute; left: 0; top: 52px; width: 100%; height: 5px;
    background: linear-gradient(90deg, var(--maroon-soft), var(--maroon) 45%, var(--maroon));
  }
  .letterhead .brand-mark { left: 118px; top: 32px; width: 104px; height: 44px; font-size: 15px; }
  .letterhead .signoff {
    position: absolute; right: 18px; bottom: 52px; text-align: right; color: var(--maroon);
  }
  .signoff .company { font-size: 15px; font-weight: 600; }
  .signoff .trade { font-size: 10px; font-weight: 600; margin-top: 2px; }
  .letterhead .bottom-rule {
    position: absolute; right: 0; bottom: 44px; width: 160px; height: 4px; background: var(--maroon);
  }

  /* Folder */
  .folder { position: absolute; left: 420px; top: 130px; width: 740px; height: 610px; }
  .folder .pocket { position: absolute; left: 0; top: 0; width: 740px; height: 610px; }
  .folder-cover {
    position: absolute; left: 0; top: 0; width: 740px; height: 520px;
    background: linear-gradient(180deg, var(--silver) 0%, #e4e4e5 45%, var(--paper) 100%);
    box-shadow: 0 4px 14px rgba(0,0,0,.25);
  }
  .folder-cover .band {
    position: absolute; left: 0; top: 242px; width: 100%; height: 62px;
    background: linear-gradient(90deg, rgba(231,207,224,0) 0%, var(--maroon-soft) 20%, var(--maroon) 62%, var(--maroon));
  }
  .folder-cover .band-mark { left: 28px; top: 250px; width: 116px; height: 46px; font-size: 16px; }
  .folder-cover .team-photo {
    position: absolute; left: 395px; top: 118px; width: 315px; height: 168px;
    background: linear-gradient(90deg, #b79c7f 0%, #3a3a40 35%, #e5d8c8 60%, #9fa2a6 100%);
  }
  .folder-cover .title {
    position: absolute; right: 34px; top: 282px; text-align: right;
  }
  .folder-cover .title .company { color: var(--paper); font-size: 16px; font-weight: 600; }
  .folder-cover .title .trade { color: var(--maroon); font-size: 12px; font-weight: 600; margin-top: 8px; }
  .folder-cover .corner-mark { right: 26px; bottom: 26px; width: 104px; height: 50px; font-size: 15px; }
</style>
</head>
<body>

  <section class="letterhead" aria-label="Letterhead">
    <div class="top-rule"></div>
    <div class="brand-mark">Bright Thread</div>
    <div class="signoff">
      <p class="company">Bright Thread</p>
      <p class="trade">Embroidery</p>
    </div>
    <div class="bottom-rule"></div>
  </section>

  <section class="folder" aria-label="A4 presentation folder">
    <svg class="pocket" viewBox="0 0 740 610" aria-hidden="true">
      <path d="M0 470 H300 L300 560 L265 610 H0 Z" fill="var(--pocket-purple)"/>
    </svg>
    <div class="folder-cover">
      <div class="band"></div>
      <div class="brand-mark band-mark">Bright Thread</div>
      <div class="team-photo" role="img" aria-label="Photo of four people modelling corporate attire"></div>
      <div class="title">
        <p class="company">Bright Thread</p>
        <p class="trade">Embroidery</p>
      </div>
      <div class="brand-mark corner-mark">Bright Thread</div>
    </div>
  </section>

</body>
</html>
```